Billboard design - consider what a billboard is

Design a billboard using my logo - Billboard is 6m x 3m
A Billboard is advertising for my company that is on a big sign.

Has to be clean and easy to read, and ideally highlights that we are Residential and Commercial builders.

Keep it clean and easy to read

The contact number for the board is

022 583 7092
www.harbourframeworks.co.nz
info@harbourframeworks.co.nz

Doesnt have to have all contact details if it doesnt fit

Has to catch peoples attention to contact us if they need a builder

Can you please change the sign to be all white writing, with black background ?
Updates

Please consider what a billboard is...

The design needs to be suitable for a billboard..

Target Market(s)

people driving past

Industry/Entity Type

Construction

Logo Text

Wellington Builder, website email address, contact number

Colors
0054AA
0677BA
7BADD7
CADEEF
E8F1F8

Requirements
Must have
• Easy to read
Nice to have
• easy to read, can clearly see contact details

```html
<!DOCTYPE html>
<html lang="en">
<head>
<meta charset="UTF-8">
<title>Harbour Frameworks – Wellington Builder Billboard</title>
<link href="https://fonts.googleapis.com/css2?family=Oswald:wght@600;700&family=Open+Sans:wght@600&display=swap" rel="stylesheet">
<style>
  :root {
    --brand-blue: #5188c8;
    --brand-grey: #6d6463;
    --board-white: #ffffff;
    --backdrop: #e8f1f8;
  }
  * { margin: 0; padding: 0; box-sizing: border-box; }
  html, body {
    width: 1200px;
    height: 1000px;
    overflow: hidden;
    background: var(--backdrop);
  }
  .billboard {
    position: absolute;
    left: 0;
    top: 200px;
    width: 1200px;
    height: 600px;
    background: var(--board-white);
    color: var(--brand-blue);
  }
  .brand-name {
    position: absolute;
    left: 96px;
    top: 92px;
    display: flex;
    align-items: center;
    gap: 22px;
    font-family: "Oswald", sans-serif;
    font-weight: 600;
    color: var(--brand-blue);
  }
  .brand-mark {
    width: 34px;
    height: 150px;
    background: var(--brand-grey);
  }
  .brand-words {
    display: flex;
    flex-direction: column;
    line-height: 1;
  }
  .brand-words .line-one { font-size: 96px; letter-spacing: 1px; }
  .brand-words .line-two { font-size: 46px; letter-spacing: 3px; margin-top: 6px; }
  .divider {
    position: absolute;
    left: 565px;
    top: 109px;
    width: 3px;
    height: 192px;
    background: var(--brand-blue);
  }
  .headline {
    position: absolute;
    left: 598px;
    top: 100px;
    width: 530px;
    font-family: "Oswald", sans-serif;
    font-weight: 700;
    text-align: center;
    line-height: 1;
  }
  .headline .city {
    display: block;
    font-size: 112px;
    letter-spacing: 1px;
  }
  .headline .trade {
    display: block;
    margin-top: 18px;
    font-size: 54px;
    letter-spacing: 48px;
    margin-right: -48px;
  }
  .call-line {
    position: absolute;
    left: 0;
    top: 378px;
    width: 1200px;
    display: flex;
    justify-content: center;
    align-items: center;
    font-family: "Oswald", sans-serif;
    font-weight: 700;
    font-size: 72px;
    line-height: 1;
    gap: 0;
  }
  .call-line svg { width: 54px; height: 54px; margin-right: 22px; }
  .call-line .phone-number { margin-left: 100px; letter-spacing: 2px; }
  .contact-row {
    position: absolute;
    left: 0;
    top: 528px;
    width: 1200px;
    display: flex;
    justify-content: space-between;
    padding: 0 60px 0 50px;
    font-family: "Open Sans", sans-serif;
    font-weight: 600;
    font-size: 27px;
  }
  .contact-item { display: flex; align-items: center; gap: 22px; }
  .contact-item svg { width: 38px; height: 38px; }
</style>
</head>
<body>
  <main class="billboard">
    <div class="brand-name">
      <span class="brand-mark"></span>
      <span class="brand-words">
        <span class="line-one">HARBOUR</span>
        <span class="line-two">FRAMEWORKS</span>
      </span>
    </div>

    <span class="divider"></span>

    <h1 class="headline">
      <span class="city">WELLINGTON</span>
      <span class="trade">BUILDER</span>
    </h1>

    <div class="call-line">
      <svg viewBox="0 0 24 24" aria-hidden="true">
        <path fill="currentColor" d="M6.6 10.8a15.1 15.1 0 0 0 6.6 6.6l2.2-2.2a1 1 0 0 1 1-.25 11.4 11.4 0 0 0 3.6.57 1 1 0 0 1 1 1V20a1 1 0 0 1-1 1A17 17 0 0 1 3 4a1 1 0 0 1 1-1h3.5a1 1 0 0 1 1 1c0 1.25.2 2.45.57 3.57a1 1 0 0 1-.25 1z"/>
      </svg>
      <span class="call-label">CALL NOW</span>
      <span class="phone-number">022 583 7092</span>
    </div>

    <div class="contact-row">
      <span class="contact-item">
        <svg viewBox="0 0 24 24" aria-hidden="true">
          <rect x="2" y="5" width="20" height="14" fill="none" stroke="currentColor" stroke-width="2"/>
          <path d="M2 5l10 8 10-8M2 19l7.5-7M22 19l-7.5-7" fill="none" stroke="currentColor" stroke-width="2"/>
        </svg>
        info@harbourframeworks.co.nz
      </span>
      <span class="contact-item">
        <svg viewBox="0 0 24 24" aria-hidden="true">
          <circle cx="12" cy="12" r="10" fill="currentColor"/>
          <g fill="none" stroke="#fff" stroke-width="1.4">
            <ellipse cx="12" cy="12" rx="4.5" ry="10"/>
            <path d="M2 12h20M4 7h16M4 17h16M12 2v20"/>
          </g>
        </svg>
        www.harbourframeworks.co.nz
      </span>
    </div>
  </main>
</body>
</html>
```